Pool Services Flyer promote regular pool services

We need a flyer design to be send out as a DL Postcard

We are a pool and spa maintenance business and would like to promote of regular pool services.
Please see our website www.brightripplepoolcare.com.au and our facebook page https://www.facebook.com/pages/Bright-Ripple-Pool-Care/583920174630518

We are pretty flexible with layouts etc Our monthly pool service is $67.00 plus chemicals so we would like this highlighted on our ad. We also so one off, weekly and fortnightly services as well.

We would like our details and logo on front and website also listed.

Target Market(s)

Pool owners

Industry/Entity Type

Pool Service

Colors
33a6d7
0292cd
0555a3
3276b5
85abd2

Requirements
Must have
• Logo
• website address
• phone number
• Price
• Promote the fact that customer wont have to worry about their pool
Nice to have
• like to have a blue wave down the bottom of flyer witht eh contact information in it. Would like to to be crisp not over crowed with information

```html
<!DOCTYPE html>
<html lang="en">
<head>
<meta charset="utf-8">
<title>Bright Ripple Pool Care – DL Postcard</title>
<link rel="stylesheet" href="https://fonts.googleapis.com/css2?family=Anton&family=Oswald:wght@500;700&family=Open+Sans:wght@400&display=swap">
<style>
  :root{
    --page:#e9e6e1;
    --sky-top:#8fc3e6;
    --sky-mid:#e6f2fa;
    --pool-light:#5cc3ea;
    --pool:#0292cd;
    --pool-deep:#0555a3;
    --panel:#3276b5;
    --panel-soft:#85abd2;
    --accent:#33a6d7;
    --navy:#0c2a4a;
    --yellow:#ffe500;
    --white:#ffffff;
    --ink:#0a1a2c;
  }
  *{box-sizing:border-box;margin:0;padding:0}
  html,body{width:1200px;height:1200px;overflow:hidden}
  body{background:var(--page);position:relative;font-family:"Open Sans",sans-serif}

  .postcard{
    position:absolute;left:40px;top:336px;width:1120px;height:528px;
    overflow:hidden;background:var(--pool);
    box-shadow:0 6px 22px rgba(0,0,0,.18);
  }
  .scene-photo{
    position:absolute;inset:0;
    background:
      radial-gradient(ellipse 60% 45% at 78% 70%, rgba(150,225,250,.55), transparent 70%),
      linear-gradient(172deg,var(--sky-top) 0%,var(--sky-mid) 22%,#ffffff 30%,var(--pool-light) 40%,var(--pool) 70%,var(--pool-deep) 100%);
  }
  .decor{position:absolute;inset:0;width:100%;height:100%}

  .photo-circle{
    position:absolute;border-radius:50%;border:5px solid var(--white);
    box-shadow:0 3px 10px rgba(0,0,0,.25);
  }
  .photo-family{left:38px;top:138px;width:226px;height:226px;
    background:radial-gradient(circle at 50% 45%,#f2c89a 0%,#e7b27a 30%,#f3d34a 52%,#4eb6e4 75%,#2a8fd0 100%)}
  .photo-spa{left:170px;top:300px;width:176px;height:176px;
    background:radial-gradient(circle at 50% 50%,#f4d7c0 0%,#e9c1a2 40%,#fbfbfb 70%,#e9eef2 100%)}

  .brand{
    position:absolute;left:372px;top:28px;display:flex;align-items:center;gap:14px;white-space:nowrap;
  }
  .brand-mark{width:46px;height:46px;border-radius:50%;background:var(--accent)}
  .brand-name{font-family:"Open Sans",sans-serif;font-weight:400;font-size:34px;color:var(--ink);letter-spacing:.5px}

  .headline{
    position:absolute;left:310px;top:98px;white-space:nowrap;
    font-family:"Anton",sans-serif;font-weight:400;font-size:62px;line-height:1;color:var(--white);
    letter-spacing:1px;transform:skewX(-4deg);
    text-shadow:-3px -3px 0 var(--ink),3px -3px 0 var(--ink),-3px 3px 0 var(--ink),3px 3px 0 var(--ink),5px 5px 0 rgba(10,26,44,.55);
  }
  .services-line{
    position:absolute;left:340px;top:180px;white-space:nowrap;
    font-family:"Oswald",sans-serif;font-weight:700;font-size:22px;line-height:1;color:var(--pool-deep);letter-spacing:.5px;
  }

  .offer{position:absolute;left:362px;top:226px;display:flex;align-items:flex-start;gap:20px;white-space:nowrap}
  .offer-label,.offer-price,.offer-note{
    color:var(--yellow);
    text-shadow:-2px -2px 0 var(--ink),2px -2px 0 var(--ink),-2px 2px 0 var(--ink),2px 2px 0 var(--ink),4px 4px 0 rgba(10,26,44,.5);
  }
  .offer-label{font-family:"Anton",sans-serif;font-size:46px;line-height:1.04;margin-top:8px}
  .offer-price-wrap{display:flex;flex-direction:column;align-items:flex-start}
  .offer-price{font-family:"Anton",sans-serif;font-size:84px;line-height:1}
  .offer-price sup{font-size:36px;vertical-align:top;position:relative;top:4px}
  .offer-note{font-family:"Oswald",sans-serif;font-weight:700;font-size:22px;line-height:1;margin-top:6px;margin-left:8px}

  .contact-band{
    position:absolute;left:360px;right:0;bottom:0;height:70px;background:var(--navy);
    display:flex;align-items:center;justify-content:space-between;padding:0 24px 0 40px;white-space:nowrap;
  }
  .contact-phone{display:flex;align-items:center;gap:12px;font-family:"Oswald",sans-serif;font-weight:700;font-size:28px;color:var(--white)}
  .contact-phone svg{width:36px;height:36px;flex:none}
  .contact-web{font-family:"Oswald",sans-serif;font-weight:500;font-size:25px;color:var(--white);letter-spacing:1px;text-transform:uppercase}
</style>
</head>
<body>
  <article class="postcard">
    <div class="scene-photo" role="img" aria-label="Bright sky over a clear blue swimming pool with a steel ladder on the right"></div>

    <svg class="decor" viewBox="0 0 1120 528" aria-hidden="true">
      <path d="M0 120 C120 100 260 110 330 160 C300 240 330 330 360 400 C330 470 220 500 0 528 Z" fill="var(--panel)"/>
      <path d="M0 140 C110 118 240 126 310 170 C284 240 306 320 336 392 C300 450 200 480 0 506 Z" fill="var(--accent)" opacity=".55"/>
      <path d="M0 430 C120 400 260 420 460 470 L460 528 L0 528 Z" fill="var(--pool-deep)"/>
      <path d="M0 455 C140 425 280 450 440 500 L440 528 L0 528 Z" fill="var(--white)"/>
      <path d="M0 472 C150 446 290 470 420 515 L420 528 L0 528 Z" fill="var(--pool)"/>
      <path d="M0 494 C130 476 250 492 360 528 L0 528 Z" fill="var(--white)"/>
      <path d="M0 506 C110 494 210 506 290 528 L0 528 Z" fill="var(--panel-soft)"/>
    </svg>

    <div class="photo-circle photo-family" role="img" aria-label="Family relaxing on a yellow pool float"></div>
    <div class="photo-circle photo-spa" role="img" aria-label="Woman enjoying a relaxing spa massage"></div>

    <div class="brand">
      <span class="brand-mark"></span>
      <span class="brand-name">Bright Ripple Pool Care</span>
    </div>

    <h1 class="headline">POOL N' SPA MAINTENANCE</h1>
    <p class="services-line">FOR A ONE OFF, WEEKLY AND FORTNIGHTLY SERVICES</p>

    <div class="offer">
      <p class="offer-label">MONTHLY<br>SERVICES</p>
      <div class="offer-price-wrap">
        <p class="offer-price">$67<sup>.00</sup></p>
        <p class="offer-note">PLUS CHEMICALS</p>
      </div>
    </div>

    <footer class="contact-band">
      <span class="contact-phone">
        <svg viewBox="0 0 40 40" aria-hidden="true">
          <rect x="4" y="14" width="32" height="22" rx="4" fill="var(--white)"/>
          <path d="M2 14 C2 4 38 4 38 14 L30 16 L28 11 C22 9 18 9 12 11 L10 16 Z" fill="var(--white)"/>
          <circle cx="20" cy="25" r="6" fill="var(--navy)"/>
        </svg>
        (02) 4810 3572
      </span>
      <span class="contact-web">www.brightripplepoolcare.com.au</span>
    </footer>
  </article>
</body>
</html>
```